Eye Catching Email Marketing design

Our health care consulting firm is based in New York City. We sell health care consulting Services to medical practices (doctors). We need a powerful email marketing design to use as one of our primary selling tools to attract new clients. The Design should convey health care knowledge, expertise professionalism, cutting edge technology and the services we offer. <br/>The design should incorporate our logo and its colors (blue and white) but we want it to be eye catching and vibrant, so other colors be included. We are open to the designer's creativity. Any pictures used should show diversity (races)and should include women. Designers can find our logo and other graphics on our website at www larkfield advisory group.com. Please feel free to ask questions.<br/><br/>

Target Market(s)

Health care professionals, executives and Doctors.

Colors

Designer to choose colors to be used in the design.

Requirements
Nice to have
• What ever the design feels will help make this design vibrant

```html
<!DOCTYPE html>
<html lang="en">
<head>
<meta charset="utf-8">
<title>Larkfield Advisory Group — Healthcare Operations Newsletter</title>
<link href="https://fonts.googleapis.com/css2?family=Montserrat:wght@400;500;600;700&display=swap" rel="stylesheet">
<style>
:root{
  --orange:#f7850a;
  --sky:#35a7d9;
  --navy:#0b55a6;
  --ink-blue:#1b6fb8;
  --white:#ffffff;
  --photo-warm:#d9d4cc;
  --photo-cool:#c9d6e0;
}
*{box-sizing:border-box;margin:0;padding:0}
html,body{width:1200px;height:4528px;overflow:hidden;background:var(--white);font-family:"Montserrat",sans-serif}
.canvas{position:relative;width:1200px;height:4528px}
.block{position:absolute;left:171px;width:847px}
.half{position:absolute;top:0;width:424px;height:100%}
.half.left{left:0}.half.right{left:423px}
.photo{background:linear-gradient(135deg,var(--photo-cool),var(--photo-warm))}
.btn{display:inline-block;font-size:17px;padding:0 28px;height:57px;line-height:57px;text-align:center}
.btn.light{background:var(--white);color:var(--ink-blue)}
.btn.light.orange-text{color:var(--orange)}
.btn.sky{background:var(--sky);color:var(--white)}
.rule{position:absolute;height:2px}

/* top bar */
.topbar{position:absolute;top:0;left:171px;width:847px;height:53px;display:flex;justify-content:space-around;align-items:center;font-size:14px;color:var(--orange);border-bottom:2px solid var(--sky)}
.topbar span{display:flex;align-items:center;gap:6px}
.brand{position:absolute;top:84px;left:0;width:1200px;text-align:center;color:var(--navy)}
.brand .name{font-size:38px;font-weight:700;letter-spacing:1px}
.brand .sub{font-size:12px;font-weight:500;letter-spacing:1px;color:#333;margin-top:4px}

/* hero */
.hero-photo{top:174px;height:414px}
.hero-band{top:588px;height:301px;background:var(--orange);color:var(--white);text-align:center}
.hero-band h1{font-weight:500;font-size:31px;letter-spacing:1px;padding-top:22px}
.hero-band .bar{width:222px;height:2px;background:var(--white);margin:18px auto 0}
.hero-band p{font-size:16px;line-height:28px;margin:24px auto 0;width:720px}
.hero-band .btn{margin-top:24px;width:155px;padding:0}

/* welcome */
.welcome{top:889px;height:520px}
.welcome .copy{position:absolute;left:438px;top:84px;width:400px}
.welcome h2{font-size:40px;font-weight:500;color:var(--sky)}
.welcome h3{font-size:38px;font-weight:600;color:var(--orange);line-height:44px;margin-top:10px}
.welcome p{font-size:17px;line-height:28px;color:var(--ink-blue);margin-top:18px}
.welcome .btn{margin-top:28px;width:156px;padding:0}

/* split features */
.split{height:437px}
.panel{color:var(--white)}
.panel.sky{background:var(--sky)}
.panel.orange{background:var(--orange)}
.panel h4{font-size:31px;font-weight:600}
.panel p{font-size:17px;line-height:28px}
.feature-a{top:1450px}
.feature-a .panel{padding:82px 28px 0 28px}
.feature-a h4{margin-left:4px}
.feature-a p{margin-top:20px}
.feature-a .btn{margin:26px 0 0 108px;width:155px;padding:0}
.feature-b{top:1887px;height:519px}
.feature-b .panel{text-align:center;padding-top:64px}
.checks{list-style:none;text-align:left;display:inline-block;margin-top:24px}
.checks li{font-size:17px;line-height:37px;display:flex;align-items:center;gap:8px}
.feature-b .btn{display:block;margin:24px auto 0;width:155px;padding:0}

/* services */
.services{top:2449px;height:407px;background:var(--sky);color:var(--white);text-align:center}
.services h4{font-size:31px;font-weight:600;padding-top:52px}
.services p{font-size:17px;line-height:28px;width:760px;margin:22px auto 0}
.services .bar{width:404px;height:2px;background:var(--white);margin:28px auto 0}
.service-row{display:flex;justify-content:space-between;padding:0 22px;margin-top:24px}
.service{width:190px;font-size:17px;font-weight:700;line-height:22px;letter-spacing:-.5px}
.service svg{display:block;margin:0 auto 22px}

/* cards */
.cards{top:2882px;height:414px;background:var(--navy);display:flex;justify-content:space-between;padding:20px 14px 0}
.card{width:256px;text-align:center;color:var(--white)}
.card .photo{height:203px}
.card p{font-size:17px;line-height:22px;margin-top:40px}
.card .btn{margin-top:24px;width:155px;padding:0;color:var(--sky)}

/* lab */
.lab{top:3337px;height:492px}
.lab .panel{padding:78px 28px 0 14px}
.lab h4{font-size:32px}
.lab p{margin:50px 0 0 14px}

/* closing */
.closing{top:3829px;height:542px}
.closing .copy{position:absolute;left:465px;top:68px;width:360px;color:var(--ink-blue)}
.closing h4{font-size:33px;font-weight:600;color:var(--orange)}
.closing p{font-size:17px;line-height:33px;margin-top:12px}
.closing .regards{font-size:17px;margin-top:28px}
.signature{width:260px;height:112px;margin-top:6px;background:linear-gradient(90deg,#eef2f7,#ffffff)}
.closing .role{font-size:17px;font-weight:600;color:var(--orange);margin-top:6px}

/* footer */
.footer{top:4371px;height:157px;background:var(--navy);text-align:center;color:var(--white)}
.social{display:flex;justify-content:center;gap:28px;padding-top:30px}
.social span{width:42px;height:42px;border:2px solid var(--white);border-radius:50%}
.footer .links{font-size:14px;margin-top:36px}
</style>
</head>
<body>
<div class="canvas">

  <header class="topbar">
    <span><svg width="12" height="14" viewBox="0 0 12 14"><path d="M6 0a5 5 0 0 0-5 5c0 4 5 9 5 9s5-5 5-9a5 5 0 0 0-5-5z" fill="#f7850a"/></svg>Your Address</span>
    <span><svg width="15" height="11" viewBox="0 0 15 11"><rect x=".5" y=".5" width="14" height="10" fill="none" stroke="#9aa" /><path d="M1 1l6.5 5L14 1" fill="none" stroke="#9aa"/></svg>info@example.com</span>
    <span><svg width="10" height="13" viewBox="0 0 10 13"><path d="M1 0v13M1 1h8v5H1" fill="none" stroke="#9aa"/></svg>www.example.com</span>
    <span><svg width="14" height="12" viewBox="0 0 14 12"><rect x="1" y="3" width="12" height="9" rx="2" fill="#d93030"/><rect x="0" y="0" width="14" height="4" rx="2" fill="#d93030"/></svg>+1 234 56789</span>
  </header>

  <div class="brand">
    <div class="name">Larkfield</div>
    <div class="sub">LARKFIELD ADVISORY GROUP LLC</div>
  </div>

  <div class="block hero-photo photo" role="img" aria-label="Photo of a diverse team of doctors and consultants meeting around a table in a bright office"></div>
  <section class="block hero-band">
    <h1>ADVANCING HEALTHCARE OPERATIONS</h1>
    <div class="bar"></div>
    <p>Lorem ipsum dolor sit amet, consectetur adipiscing elit, sed do eiusmod tempor incididunt ut labore et dolore magna aliqua.</p>
    <a class="btn light">Read More</a>
  </section>

  <section class="block welcome">
    <div class="half left photo" role="img" aria-label="Photo of a smiling female doctor holding a tablet with colleagues behind her"></div>
    <div class="copy">
      <h2>Welcome</h2>
      <h3>Larkfield Advisory Group</h3>
      <p>Lorem ipsum dolor sit amet, consectetur adipiscing elit, sed do eiusmod tempor incididunt ut labore et dolore magna.</p>
      <a class="btn sky">Read More</a>
    </div>
  </section>

  <div class="rule" style="top:1427px;left:309px;width:573px;background:var(--orange)"></div>

  <section class="block split feature-a">
    <div class="half left panel sky">
      <h4>Lorem Ipsum</h4>
      <p>Lorem ipsum dolor sit amet, consectetur adipiscing elit, sed do eiusmod tempor incididunt ut labore et dolore magna.</p>
      <a class="btn light">Read More</a>
    </div>
    <div class="half right photo" role="img" aria-label="Photo of a long hospital corridor with medical staff walking"></div>
  </section>

  <section class="block feature-b">
    <div class="half left photo" role="img" aria-label="Photo of a smiling nurse in scrubs and cap with a stethoscope"></div>
    <div class="half right panel orange">
      <h4>Lorem Ipsum</h4>
      <ul class="checks">
        <li><svg width="18" height="16" viewBox="0 0 18 16"><path d="M2 8l5 5L16 2" fill="none" stroke="#333" stroke-width="3"/></svg>Lorem ipsum dolor sit amet</li>
        <li><svg width="18" height="16" viewBox="0 0 18 16"><path d="M2 8l5 5L16 2" fill="none" stroke="#333" stroke-width="3"/></svg>Lorem ipsum dolor sit amet</li>
        <li><svg width="18" height="16" viewBox="0 0 18 16"><path d="M2 8l5 5L16 2" fill="none" stroke="#333" stroke-width="3"/></svg>Lorem ipsum dolor sit amet</li>
        <li><svg width="18" height="16" viewBox="0 0 18 16"><path d="M2 8l5 5L16 2" fill="none" stroke="#333" stroke-width="3"/></svg>Lorem ipsum dolor sit amet</li>
      </ul>
      <a class="btn light orange-text">Read More</a>
    </div>
  </section>

  <div class="rule" style="top:2427px;left:288px;width:616px;background:var(--sky)"></div>

  <section class="block services">
    <h4>Lorem Ipsum</h4>
    <p>Lorem ipsum dolor sit amet, consectetur adipiscing elit, sed do eiusmod tempor incididunt ut labore et dolore magna.</p>
    <div class="bar"></div>
    <div class="service-row">
      <div class="service"><svg width="70" height="70" viewBox="0 0 70 70"><path d="M35 10a25 25 0 1 1-23 15" fill="none" stroke="#fff" stroke-width="7"/><path d="M6 18l8 12 10-10z" fill="#fff"/></svg>REVENUE CYCLE MANAGEMENT</div>
      <div class="service"><svg width="70" height="70" viewBox="0 0 70 70"><rect x="16" y="8" width="38" height="54" rx="4" fill="none" stroke="#fff" stroke-width="5"/><path d="M25 36l7 7 13-15" fill="none" stroke="#fff" stroke-width="5"/></svg>COMPLIANCE MANAGEMENT</div>
      <div class="service"><svg width="70" height="70" viewBox="0 0 70 70"><circle cx="35" cy="20" r="10" fill="none" stroke="#fff" stroke-width="5"/><path d="M8 40l14 20h26l14-20" fill="none" stroke="#fff" stroke-width="5"/></svg>HEALTHCARE INNOVATION</div>
      <div class="service"><svg width="70" height="70" viewBox="0 0 70 70"><circle cx="35" cy="35" r="22" fill="none" stroke="#fff" stroke-width="9" stroke-dasharray="9 5"/><circle cx="35" cy="35" r="8" fill="#fff"/></svg>PRACTICE MANAGEMENT</div>
    </div>
  </section>

  <section class="block cards">
    <div class="card"><div class="photo" role="img" aria-label="Photo of dental instruments on a clinic tray"></div><p>I'm a new Text block ready for your content.</p><a class="btn light">Read More</a></div>
    <div class="card"><div class="photo" role="img" aria-label="Photo of surgeons operating under theatre lights"></div><p>I'm a new Text block ready for your content.</p><a class="btn light">Read More</a></div>
    <div class="card"><div class="photo" role="img" aria-label="Photo of doctors reviewing an X-ray together"></div><p>I'm a new Text block ready for your content.</p><a class="btn light">Read More</a></div>
  </section>

  <div class="rule" style="top:3316px;left:288px;width:616px;background:var(--sky)"></div>

  <section class="block split lab">
    <div class="half left panel orange">
      <h4>Lorem Ipsum</h4>
      <p>Lorem ipsum dolor sit amet, consectetur adipiscing elit, sed do eiusmod tempor incididunt ut labore dolore magna lorem.</p>
    </div>
    <div class="half right photo" role="img" aria-label="Photo of a pipette filling test tubes in a green rack in a laboratory"></div>
  </section>

  <section class="block closing">
    <div class="half left photo" role="img" aria-label="Portrait photo of a female executive in a white blazer"></div>
    <div class="copy">
      <h4>Lorem ipsum</h4>
      <p>Lorem ipsum dolor sit amet, consectetur adipiscing elit, sed do eiusmod tempor incididunt ut labore et dolore magna. Sed ut perspiciatis unde omnis iste.</p>
      <div class="regards">Kind Regards,</div>
      <div class="signature" role="img" aria-label="Handwritten signature"></div>
      <div class="role">CEO, COMPANY NAME</div>
    </div>
  </section>

  <footer class="block footer">
    <div class="social" role="img" aria-label="Social media links">
      <span></span><span></span><span></span><span></span>
    </div>
    <div class="links">Unsubscribe &nbsp;|&nbsp; View Online</div>
  </footer>

</div>
</body>
</html>
```